Tallowmoor Letterheads Design

Hello, we have just upgraded this project for a guaranteed payment.

We are currently going through a re-branding exercise internally. Our logo is attached as a PDF file.

We are happy with our logo but would like to investigate how we can best apply the logo to our letterheads and compliment slips.

We are a quality printing company in England. Despite our name we are very professional and offer a personal service.

Our new website is under construction and here is a link to show you how it looks: http://brackenpress.v4ntor.co.uk

The style must be professional and steer away from "tacky" otherwise it makes our company look very low budget and just a bit silly.

We would like to see elements of creativity though, so please, nothing too boring.

I have attached our new logo, there is an option for use on white or black.

Cheers
Tallowmoor Team

Reason: We have increased the deadline due to an internal delay to things, we now have more time before we need anything to be printed.

Industry/Entity Type

Construction

Requirements
Must have
• IMPORTANT! Please do not tweak or change our logo in any way. A few designs show vast changes in the logo, this is not what we require. Please do not change the logo in any way. Thanks
Nice to have
• Classy but approachable. Elements of "quirky" would be nice to see.
Should not have
• A Tacky feel

```html
<!DOCTYPE html>
<html lang="en">
<head>
<meta charset="utf-8">
<title>Tallowmoor Letterheads</title>
<link rel="stylesheet" href="https://fonts.googleapis.com/css2?family=Archivo+Black&family=Open+Sans:wght@400;600;700&display=swap">
<style>
  :root {
    --backdrop: #1d1d1d;
    --paper: #ffffff;
    --brand-pink: #ee2372;
    --brand-pink-light: #f2477f;
    --ink: #1f1f1f;
    --muted: #6b6b6b;
    --soft-grey: #e8eced;
    --soft-pink: #fbe1e9;
  }
  * { margin: 0; padding: 0; box-sizing: border-box; }
  html, body { width: 1200px; height: 900px; overflow: hidden; }
  body {
    background: var(--backdrop);
    font-family: "Open Sans", Arial, sans-serif;
    position: relative;
  }
  .option-title {
    position: absolute;
    top: 24px;
    font-family: "Archivo Black", Arial, sans-serif;
    font-size: 38px;
    color: var(--paper);
    letter-spacing: 0.5px;
    transform: translateX(-50%);
  }
  .option-title--two { left: 325px; }
  .option-title--three { left: 898px; }

  .letterhead {
    position: absolute;
    background: var(--paper);
    overflow: hidden;
  }
  .letterhead--two { left: 37px; top: 90px; width: 544px; height: 768px; }
  .letterhead--three { left: 624px; top: 86px; width: 547px; height: 776px; }

  .brand {
    position: absolute;
    left: 28px;
    top: 30px;
    width: 150px;
    text-align: center;
  }
  .brand__dot {
    display: block;
    width: 44px;
    height: 44px;
    margin: 0 auto 12px;
    border-radius: 50%;
    background: var(--brand-pink);
  }
  .brand__name {
    display: block;
    font-weight: 700;
    font-size: 25px;
    line-height: 1;
    color: var(--ink);
    letter-spacing: -0.4px;
  }
  .brand__tagline {
    display: block;
    margin-top: 5px;
    font-size: 11px;
    color: var(--ink);
  }

  .contact {
    position: absolute;
    left: 368px;
    top: 49px;
    list-style: none;
    font-size: 10px;
    line-height: 13px;
    color: var(--muted);
  }
  .letterhead--three .contact { left: 372px; top: 50px; }
  .contact__item { display: flex; align-items: center; gap: 3px; white-space: nowrap; }
  .contact__icon { width: 9px; height: 9px; flex: none; }

  .mascot-backdrop {
    position: absolute;
    left: 278px;
    top: 440px;
    width: 266px;
    height: 280px;
    border-radius: 45% 45% 10% 10%;
    background: radial-gradient(ellipse at 45% 40%, var(--soft-pink) 0%, #fdf2f5 45%, var(--soft-grey) 75%, rgba(255,255,255,0) 100%);
    opacity: 0.8;
  }

  .footer-band {
    position: absolute;
    left: 0;
    bottom: 0;
    width: 100%;
    height: 58px;
    background: linear-gradient(180deg, var(--brand-pink-light) 0%, var(--brand-pink) 100%);
  }
  .letterhead--three .footer-band { height: 56px; }
</style>
</head>
<body>
  <h2 class="option-title option-title--two">OPTION-2</h2>
  <h2 class="option-title option-title--three">OPTION-3</h2>

  <section class="letterhead letterhead--two">
    <div class="brand">
      <span class="brand__dot"></span>
      <span class="brand__name">Tallowmoor</span>
      <span class="brand__tagline">Quality Printing</span>
    </div>
    <ul class="contact">
      <li class="contact__item">
        <svg class="contact__icon" viewBox="0 0 10 10"><path d="M2 0.5 L4 2.5 L3 4 Q4.5 6 6 7 L7.5 6 L9.5 8 L8 9.5 Q3 9 0.5 2 Z" fill="#ee2372"/></svg>
        0208 555 0172
      </li>
      <li class="contact__item">
        <svg class="contact__icon" viewBox="0 0 10 10"><rect x="0.5" y="2" width="9" height="6.5" fill="#ee2372"/><path d="M0.5 2 L5 5.5 L9.5 2" stroke="#fff" stroke-width="1" fill="none"/></svg>
        orders@tallowmoor.co.uk
      </li>
      <li class="contact__item">
        <svg class="contact__icon" viewBox="0 0 10 10"><circle cx="5" cy="5" r="4.5" fill="#ee2372"/><path d="M0.5 5 H9.5 M5 0.5 Q2 5 5 9.5 M5 0.5 Q8 5 5 9.5" stroke="#fff" stroke-width="0.8" fill="none"/></svg>
        www.brackenpress.v4ntor.co.uk
      </li>
    </ul>

    <div class="mascot-backdrop" role="img" aria-label="Large faint brand mascot decoration in soft pink and grey"></div>

    <div class="footer-band" role="img" aria-label="Pink decorative cloud band along the foot of the page"></div>
  </section>

  <section class="letterhead letterhead--three">
    <div class="brand">
      <span class="brand__dot"></span>
      <span class="brand__name">Tallowmoor</span>
      <span class="brand__tagline">Quality Printing</span>
    </div>
    <ul class="contact">
      <li class="contact__item">
        <svg class="contact__icon" viewBox="0 0 10 10"><path d="M2 0.5 L4 2.5 L3 4 Q4.5 6 6 7 L7.5 6 L9.5 8 L8 9.5 Q3 9 0.5 2 Z" fill="#ee2372"/></svg>
        0208 555 0172
      </li>
      <li class="contact__item">
        <svg class="contact__icon" viewBox="0 0 10 10"><rect x="0.5" y="2" width="9" height="6.5" fill="#ee2372"/><path d="M0.5 2 L5 5.5 L9.5 2" stroke="#fff" stroke-width="1" fill="none"/></svg>
        orders@tallowmoor.co.uk
      </li>
      <li class="contact__item">
        <svg class="contact__icon" viewBox="0 0 10 10"><circle cx="5" cy="5" r="4.5" fill="#ee2372"/><path d="M0.5 5 H9.5 M5 0.5 Q2 5 5 9.5 M5 0.5 Q8 5 5 9.5" stroke="#fff" stroke-width="0.8" fill="none"/></svg>
        www.brackenpress.v4ntor.co.uk
      </li>
    </ul>

    <div class="footer-band" role="img" aria-label="Pink outlined decorative cloud band along the foot of the page"></div>
  </section>
</body>
</html>
```